Business Cards for Law Office of Denise R. Harlow

I need a business card for my new estate planning law firm. I have attached my logo. I would like a design that is professional but not too formal or stuffy.

Target Market(s)

Professionals (lawyers, doctors, businesswomen) between the age of 30 and 50 who are tech-savvy and educated.

Industry/Entity Type

Lawyer

Contact Information for Business Card

Denise R. Harlow

528 E. 19th Street
7th Floor
New York, NY 10583

Phone: (855) 602-7318
Direct: (917) 463-5071
Email: Denise@DeniseRHarlowLegal.test
www.DeniseRHarlowLegal.test

Font styles to use
Other font styles liked:
• Corbel

Requirements
Must have
• On the front:
• Denise R. Harlow, Esq.
• Owner & Founder
• 528 E. 19th Street
• 7th Floor
• New York, NY 10583
• Phone: (855) 602-7318
• Direct: (917) 463-5071
• Email: denise@deniserharlowlegal.test
• www.deniserharlowlegal.test
• On the back:
• LOGO
Nice to have
• I want it to be professional but not too formal or stuffy. Please choose colors that go with my logo.
Should not have
• I don't want TOO MUCH color. Some color is good, but not too much.

```html
<!DOCTYPE html>
<html lang="en">
<head>
<meta charset="utf-8">
<title>Business Cards – Law Office of Denise R. Harlow</title>
<link href="https://fonts.googleapis.com/css2?family=Lato:wght@400;700&display=swap" rel="stylesheet">
<style>
  :root {
    --purple: #7a2a80;
    --orange: #f0892a;
    --ink: #1f1f1f;
    --paper: #ffffff;
    --backdrop: #3b3b3d;
  }
  * { box-sizing: border-box; margin: 0; padding: 0; }
  html, body { width: 1200px; height: 800px; overflow: hidden; }
  body {
    background: var(--backdrop);
    font-family: "Lato", sans-serif;
    position: relative;
  }
  .card {
    position: absolute;
    width: 525px;
    height: 300px;
    background: var(--paper);
    overflow: hidden;
    box-shadow: 0 0 0 1px rgba(0,0,0,.1);
  }
  .card--back { left: 80px; top: 100px; }
  .card--front { left: 595px; top: 400px; }

  .brand-name {
    font-family: "Lato", sans-serif;
    font-weight: 700;
    color: var(--purple);
    display: flex;
    align-items: center;
    gap: 10px;
    letter-spacing: .02em;
  }
  .brand-name__mark {
    width: 12px; height: 12px;
    background: var(--orange);
    flex: none;
  }
  .card--back .brand-name {
    position: absolute;
    left: 0; right: 0; top: 104px;
    justify-content: center;
    font-size: 26px;
  }
  .card--back .website {
    position: absolute;
    left: 0; right: 0; bottom: 42px;
    text-align: center;
    font-size: 15px;
    letter-spacing: .04em;
    color: var(--ink);
  }

  .card--front .accent-line {
    position: absolute;
    left: 22px; top: 0; bottom: 0;
    width: 3px;
    background: var(--orange);
  }
  .card--front .name-panel {
    position: absolute;
    left: 28px; top: 0; bottom: 0;
    width: 222px;
    background: var(--purple);
    padding: 30px 18px;
  }
  .person-name {
    color: var(--orange);
    font-weight: 700;
    font-size: 17px;
  }
  .person-title {
    color: var(--paper);
    font-size: 14px;
    margin-top: 4px;
  }
  .card--front .brand-name {
    position: absolute;
    right: 20px; top: 34px;
    font-size: 15px;
    gap: 7px;
  }
  .card--front .brand-name__mark { width: 9px; height: 9px; }
  .contact {
    position: absolute;
    left: 272px; top: 150px;
    font-size: 14px;
    line-height: 1.3;
    color: var(--ink);
  }
  .contact address { font-style: normal; margin-bottom: 8px; }
  .contact-row { display: flex; align-items: center; gap: 8px; }
  .contact-row svg { width: 12px; height: 12px; fill: var(--purple); flex: none; }
</style>
</head>
<body>

<section class="card card--back" aria-label="Card back">
  <div class="brand-name"><span class="brand-name__mark"></span>Law Office of Denise R. Harlow</div>
  <p class="website">www.deniserharlowlegal.test</p>
</section>

<section class="card card--front" aria-label="Card front">
  <div class="accent-line"></div>
  <div class="name-panel">
    <p class="person-name">Denise R. Harlow, Esq.</p>
    <p class="person-title">Owner &amp; Founder</p>
  </div>
  <div class="brand-name"><span class="brand-name__mark"></span>Law Office of Denise R. Harlow</div>
  <div class="contact">
    <address>
      528 E. 19th Street<br>
      7th Floor<br>
      New York, NY 10583
    </address>
    <p class="contact-row">
      <svg viewBox="0 0 24 24" aria-hidden="true"><path d="M6.6 10.8a15.1 15.1 0 0 0 6.6 6.6l2.2-2.2a1 1 0 0 1 1-.25 11.4 11.4 0 0 0 3.6.57 1 1 0 0 1 1 1V20a1 1 0 0 1-1 1A17 17 0 0 1 3 4a1 1 0 0 1 1-1h3.5a1 1 0 0 1 1 1c0 1.25.2 2.45.57 3.57a1 1 0 0 1-.25 1z"/></svg>
      (855) 602-7318
    </p>
    <p class="contact-row">
      <svg viewBox="0 0 24 24" aria-hidden="true"><path d="M6.6 10.8a15.1 15.1 0 0 0 6.6 6.6l2.2-2.2a1 1 0 0 1 1-.25 11.4 11.4 0 0 0 3.6.57 1 1 0 0 1 1 1V20a1 1 0 0 1-1 1A17 17 0 0 1 3 4a1 1 0 0 1 1-1h3.5a1 1 0 0 1 1 1c0 1.25.2 2.45.57 3.57a1 1 0 0 1-.25 1z"/></svg>
      (917) 463-5071 (direct)
    </p>
    <p class="contact-row">
      <svg viewBox="0 0 24 24" aria-hidden="true"><path d="M2 5h20v14H2zm2 2v.5l8 5 8-5V7zm0 2.8V17h16V9.8l-8 5z"/></svg>
      denise@deniserharlowlegal.test
    </p>
  </div>
</section>

</body>
</html>
```